Business card for auto dealership

Looking for a clean modern design.
Would like attached logo incorporated

Industry/Entity Type

Car dealership

Contact Information for Business Card

Name, website, phone, cell, fax, email

```html
<!DOCTYPE html>
<html lang="en">
<head>
<meta charset="utf-8">
<title>Halvorsen Truck &amp; Auto Sales – Business Card</title>
<link href="https://fonts.googleapis.com/css2?family=Barlow:wght@400;600&family=Oleo+Script&display=swap" rel="stylesheet">
<style>
  :root {
    --page-bg: #2b2d2e;
    --card-bg: #1f1f1f;
    --gloss-ink: #0b0b0b;
    --ink-light: #ffffff;
    --ink-soft: #e6e6e6;
    --rule: #d9d9d9;
  }
  * { box-sizing: border-box; margin: 0; padding: 0; }
  html, body {
    width: 1200px; height: 939px; overflow: hidden;
    background: var(--page-bg);
    font-family: "Barlow", Arial, sans-serif;
  }
  .sheet {
    width: 1200px; height: 939px;
    display: flex; flex-direction: column;
    align-items: center; justify-content: center; gap: 56px;
  }
  .card {
    width: 620px; height: 354px;
    background: var(--card-bg);
    position: relative;
    box-shadow: 0 14px 30px rgba(0,0,0,.45);
  }
  .card--front { display: flex; align-items: center; justify-content: center; }
  .brand { display: flex; flex-direction: column; line-height: 1; }
  .brand__name {
    font-family: "Barlow", Arial, sans-serif;
    font-weight: 600; font-size: 52px; letter-spacing: .5px;
  }
  .brand__tag {
    font-weight: 600; font-size: 15px; letter-spacing: 2px;
    margin-top: 6px; text-transform: uppercase;
  }
  .card--front .brand { color: var(--gloss-ink); }
  .card--back .brand { color: var(--ink-light); }
  .card--back .brand__name { font-size: 40px; }
  .card--back .brand__tag { font-size: 12px; }

  .card--back { display: flex; align-items: center; padding: 0 40px 0 48px; }
  .card--back .brand { width: 250px; }
  .divider { width: 1px; height: 230px; background: var(--rule); margin: 0 34px 0 18px; }
  .contact { color: var(--ink-light); }
  .contact__name { font-family: "Oleo Script", cursive; font-size: 30px; font-weight: 400; }
  .contact__role {
    font-size: 14px; color: var(--ink-soft);
    padding: 2px 0 6px; border-bottom: 1px solid var(--rule);
    display: inline-block; width: 96px; margin-bottom: 10px;
  }
  .contact__list { list-style: none; }
  .contact__item {
    display: flex; align-items: center; gap: 10px;
    font-size: 15px; letter-spacing: 1.5px; margin-bottom: 7px;
  }
  .contact__item svg { width: 15px; height: 15px; fill: var(--ink-light); flex: none; }
</style>
</head>
<body>
<main class="sheet">
  <section class="card card--front" aria-label="Card front">
    <div class="brand">
      <span class="brand__name">Halvorsen</span>
      <span class="brand__tag">Truck &amp; Auto Sales</span>
    </div>
  </section>

  <section class="card card--back" aria-label="Card back">
    <div class="brand">
      <span class="brand__name">Halvorsen</span>
      <span class="brand__tag">Truck &amp; Auto Sales</span>
    </div>
    <div class="divider"></div>
    <div class="contact">
      <h1 class="contact__name">Dana Halvorsen</h1>
      <p class="contact__role">Founder</p>
      <ul class="contact__list">
        <li class="contact__item">
          <svg viewBox="0 0 16 16" aria-hidden="true"><path d="M3.5 1l3 3-1.5 2c1 2 3 4 5 5l2-1.5 3 3-2 2C7 14 2 9 1.5 3.5z"/></svg>
          555-010-4011
        </li>
        <li class="contact__item">
          <svg viewBox="0 0 16 16" aria-hidden="true"><path d="M4 0h8a1 1 0 0 1 1 1v14a1 1 0 0 1-1 1H4a1 1 0 0 1-1-1V1a1 1 0 0 1 1-1zm0 2v11h8V2z"/></svg>
          555-010-2140
        </li>
        <li class="contact__item">
          <svg viewBox="0 0 16 16" aria-hidden="true"><path d="M4 0h7v4H4zM1 5h14v10H1zm2 3v2h3V8zm0 3v2h3v-2zm6-3v2h4V8zm0 3v2h4v-2z"/></svg>
          555-010-1774
        </li>
        <li class="contact__item">
          <svg viewBox="0 0 16 16" aria-hidden="true"><path d="M0 3h16v10H0zm1.5 1.2L8 9l6.5-4.8V4h-13z"/></svg>
          dana@halvorsenauto.com
        </li>
        <li class="contact__item">
          <svg viewBox="0 0 16 16" aria-hidden="true"><path d="M8 0a8 8 0 1 0 0 16A8 8 0 0 0 8 0zm0 1.5c1 0 2 2 2.3 5.5H5.7C6 3.5 7 1.5 8 1.5zM1.6 7h2.6c.1-2 .5-3.7 1.1-4.8A6.5 6.5 0 0 0 1.6 7zm10.2 0h2.6a6.5 6.5 0 0 0-3.7-4.8c.6 1.1 1 2.8 1.1 4.8zM1.6 9a6.5 6.5 0 0 0 3.7 4.8C4.7 12.7 4.3 11 4.2 9zm4.1 0C6 12.5 7 14.5 8 14.5s2-2 2.3-5.5zm6.1 0c-.1 2-.5 3.7-1.1 4.8A6.5 6.5 0 0 0 14.4 9z"/></svg>
          www.halvorsenauto.com
        </li>
      </ul>
    </div>
  </section>
</main>
</body>
</html>
```